Medical Waste Company with Logo

Need a business card design that targets office managers in the medical community. This card will be the front line for our sales team to market our services to the community. We would like to have email, phone number, website. Please use the logo attached to create a design that we would be proud of.

Target Market(s)

Medical Clients

Industry/Entity Type

Medical Supply

Contact Information for Business Card

Please use logo attached

Colors

Designer to choose colors to be used in the design.

Requirements
Must have
• Our logo (see attached file)
Nice to have
• Maybe a pop of some sort, raised..?

```html
<!DOCTYPE html>
<html lang="en">
<head>
<meta charset="utf-8">
<title>Northpeak Medical Disposal – Business Card</title>
<link href="https://fonts.googleapis.com/css2?family=Rokkitt:wght@400;500;600&family=Montserrat:wght@600&display=swap" rel="stylesheet">
<style>
  :root {
    --page-bg: #e6e6e6;
    --card-white: #ffffff;
    --navy-light: #345f90;
    --navy-dark: #22406b;
    --title-navy: #0e1d48;
    --arc-grey: #868789;
    --brand-blue: #39649f;
    --text-white: #ffffff;
  }
  * { margin: 0; padding: 0; box-sizing: border-box; }
  html, body {
    width: 1200px; height: 1200px; overflow: hidden;
    background: var(--page-bg);
  }
  .card {
    position: absolute; left: 100px; top: 294px;
    width: 1000px; height: 612px;
    background: var(--card-white);
    box-shadow: 0 14px 30px rgba(0,0,0,0.25);
    overflow: hidden;
  }
  .card-shapes { position: absolute; inset: 0; }
  .contact {
    position: absolute; left: 81px; top: 0;
    color: var(--text-white);
    font-family: "Rokkitt", Georgia, serif;
  }
  .contact-name {
    position: absolute; top: 128px; white-space: nowrap;
    font-size: 42px; font-weight: 500; letter-spacing: -0.5px;
  }
  .contact-role {
    position: absolute; top: 186px;
    font-size: 23px; color: var(--title-navy); font-weight: 500;
  }
  .contact-address {
    position: absolute; top: 246px; white-space: nowrap;
    font-size: 27px; line-height: 32px;
  }
  .contact-lines {
    position: absolute; top: 317px; list-style: none; white-space: nowrap;
    font-size: 25px;
  }
  .contact-lines li {
    display: flex; align-items: center; height: 40px; gap: 10px;
  }
  .contact-lines svg { width: 26px; height: 22px; flex: none; }
  .brand {
    position: absolute; left: 600px; top: 0; width: 400px; height: 612px;
    display: flex; flex-direction: column; align-items: center; justify-content: center;
    color: var(--brand-blue);
    font-family: "Rokkitt", Georgia, serif; font-weight: 600;
    text-align: center;
  }
  .brand-dot {
    width: 56px; height: 56px; border-radius: 50%;
    background: var(--brand-blue); margin-bottom: 18px;
  }
  .brand-name { font-size: 40px; line-height: 42px; letter-spacing: 1px; }
  .brand-sub { font-size: 26px; letter-spacing: 10px; margin-top: 4px; }
</style>
</head>
<body>
  <div class="card">
    <svg class="card-shapes" viewBox="0 0 1000 612" width="1000" height="612" aria-hidden="true">
      <defs>
        <linearGradient id="panelGradient" x1="0" y1="0" x2="1" y2="0">
          <stop offset="0" stop-color="var(--navy-light)"/>
          <stop offset="1" stop-color="var(--navy-dark)"/>
        </linearGradient>
      </defs>
      <path d="M0,0 H545 Q365,306 565,612 H0 Z" fill="url(#panelGradient)"/>
      <path d="M552,12 Q395,306 563,600 Q425,306 552,12 Z" fill="var(--arc-grey)"/>
    </svg>

    <div class="contact">
      <h1 class="contact-name">Dr. JOHN DOE</h1>
      <p class="contact-role">Doctor</p>
      <p class="contact-address">Dummy city<br>Dummy Country Land</p>
      <ul class="contact-lines">
        <li>
          <svg viewBox="0 0 26 22" aria-hidden="true"><path d="M2,8 Q13,0 24,8 L22,11 L18,9 L18,7 Q13,5 8,7 L8,9 L4,11 Z" fill="#fff"/><path d="M5,12 H21 L23,21 H3 Z" fill="#fff"/><circle cx="13" cy="16" r="3" fill="var(--navy-light)"/></svg>
          1-234-567890
        </li>
        <li>
          <svg viewBox="0 0 26 22" aria-hidden="true"><circle cx="13" cy="11" r="10" fill="#fff"/><path d="M7,5 Q11,7 9,11 Q12,14 10,18 M16,3 Q15,8 19,10 Q21,14 18,18" stroke="var(--navy-light)" stroke-width="2" fill="none"/></svg>
          www.northpeakdisposal.com
        </li>
        <li>
          <svg viewBox="0 0 26 22" aria-hidden="true"><rect x="1" y="4" width="24" height="15" fill="#fff"/><path d="M1,4 L13,13 L25,4 M1,19 L10,11 M25,19 L16,11" stroke="var(--navy-light)" stroke-width="1.5" fill="none"/></svg>
          john@northpeakdisposal.com
        </li>
      </ul>
    </div>

    <div class="brand">
      <div class="brand-dot"></div>
      <div class="brand-name">NORTHPEAK MEDICAL</div>
      <div class="brand-sub">DISPOSAL</div>
    </div>
  </div>
</body>
</html>
```